K P Guard Services - Alarm and CCTV installation Flyer

Need a flyer designed that grabs the attention of potential customers, we need the price to stand out the most to grab people’s attention, whether they are residential or commercial.We are a security company based in Brentwood Essex but cover London and the home counties. here is our website to take a look at www.kpguardservices.co.uk. We want them to know we install complete alarm and Cctv systems and will keep them “safe”

Target Market(s)

residential and commercial property

Colors
f37122

Requirements
Must have
• on one side
• large clear logo - professional design
• - Intruder Alarms starting from £495 + VAT. (Big text)
• - £150 discount on installations
• *terms and conditions apply (small text)
• - Not happy with your current provider? Free of charge no obligation take over survey and quotation and up to £100 off
• - CCTV systems starting from £595 + VAT (based on 2 cameras)
• K P Guard Services are always there, always available, wherever and whenever you need us.
• Large telephone number at the bottom 01632 480913
• Address / email / website as a footer * see website for details
• on second side
• large and bold
• Are you looking to keep you and your premises safe?
• - K P Guard Services install, maintain and repair all intruder alarms, CCTV, intercom and access control
• - View, control and manage your security systems anywhere in the world
• - Feel at ease with monitoring services & police response tailored to suit you and your business
• - K P Guard can takeover any existing security system and offer maintenance checks to guarantee the best performance for you and your premises
• - K P Guard understand that being security conscious is ever increasing, protecting your property and family is a number one priority
• - Our fully insured and accredited team offer quality, safety and cost efficiency throughout the whole process
• - K P Guard Services are using the latest cloud-based technology to stay connected with your home and business 24/7
• If you are looking to improve the security in your home, office or commercial property then call a member of our team today for a free quote.
• Fully insured and accredited
• Jobrater logo and NQRB Intruder and CCTV logos
• Logo somewhere on page and
• Telephone number
• Address / email / website as footer
Nice to have
• We would like to have the text saying
• Intruder alarms installed from £495 + vat the biggest text on the page. Most likely the £495 part the largest.
• Also would like “not happy with your current provider” more obvious
• We would like use our company colours - Orange/White/black

```html
<!DOCTYPE html>
<html lang="en">
<head>
<meta charset="utf-8">
<title>K P Guard Services – Alarm and CCTV Flyer</title>
<link href="https://fonts.googleapis.com/css2?family=Roboto:wght@400;500;700;900&display=swap" rel="stylesheet">
<style>
:root{
  --orange:#f37122;
  --orange-deep:#e8601a;
  --ink:#1a1a1a;
  --white:#ffffff;
  --stage:#2b2b2b;
  --photo-light:#e9eef2;
  --photo-mid:#b9c3cb;
  --photo-dark:#5d666d;
}
*{box-sizing:border-box;margin:0;padding:0}
html,body{width:1200px;height:720px;overflow:hidden;background:var(--stage)}
body{font-family:"Roboto",Arial,sans-serif;color:var(--ink);position:relative}
.flyer{position:absolute;background:var(--white);overflow:hidden}
.flyer--front{left:98px;top:32px;width:454px;height:662px}
.flyer--back{left:644px;top:30px;width:458px;height:668px}
.abs{position:absolute}
.hero{position:absolute;left:0;top:0}

/* front */
.brand-block{left:160px;top:262px;width:290px;text-align:center}
.brand-name{font-weight:900;color:var(--orange);font-size:36px;line-height:1.05;letter-spacing:.5px}
.brand-mark{display:inline-block;width:14px;height:14px;background:var(--orange);margin-right:8px;vertical-align:middle}
.price-label{font-size:15.5px;line-height:1.1;color:var(--ink)}
.price-ring{width:100px;height:104px}
.price-ring svg{position:absolute;left:0;top:0}
.price-ring .price{position:absolute;left:0;right:0;top:32px;text-align:center;font-size:16px;line-height:1.05}
.price-ring--cctv .price{top:30px;font-size:15.5px}
.tagline{left:160px;top:356px;width:290px;font-size:19.5px;line-height:1.14}
.switch-offer{left:156px;top:452px;width:132px;font-size:13.4px;line-height:1.15}
.discount-box{left:290px;top:449px;width:164px;height:98px;background:var(--orange);color:var(--white);padding:6px 10px;font-size:19px;line-height:1.06}
.footer{position:absolute;left:0;bottom:0;width:100%;height:74px;background:var(--orange)}
.footer .phone{position:absolute;left:0;top:0;width:158px;height:100%;color:var(--white);text-align:center}
.footer .phone svg{display:block;margin:8px auto 4px}
.footer .phone b{font-size:21px;font-weight:700;color:var(--ink)}
.footer .contact{position:absolute;left:160px;top:0;right:0;bottom:10px;background:var(--white);border-left:3px solid var(--orange);padding:6px 10px;font-size:10px;font-weight:700;line-height:1.95}
.contact-row{display:flex;align-items:center;gap:7px}
.contact-row svg{flex:none}

/* back */
.headline{left:168px;top:48px;width:282px;font-size:27px;font-weight:700;line-height:1.12;color:var(--ink);background:rgba(255,255,255,.7);padding:2px 6px}
.back-brand{left:26px;top:244px;font-weight:900;color:var(--orange);font-size:15px;line-height:1.1;width:130px}
.back-brand .brand-mark{width:10px;height:10px;margin-right:5px}
.points{font-size:11.4px;line-height:1.14;list-style:none}
.points li{position:relative;padding-left:13px}
.points li::before{content:"";position:absolute;left:0;top:3px;width:8px;height:8px;background:var(--orange);transform:rotate(45deg)}
.badges{left:222px;top:532px;width:228px;height:60px;display:flex;align-items:flex-start;gap:10px}
.badge-lister{width:80px;text-align:center;padding-top:6px}
.badge-lister small{display:block;font-size:5px;color:#555}
.badge-lister b{color:#c0392b;font-size:12px;font-weight:700}
.badge{text-align:center;font-size:4.5px;color:#555}
.badge i{display:block;width:30px;height:30px;border-radius:50%;border:3px solid #4a6fa5;margin:0 auto 3px}
.badge--square i{border-radius:0;width:34px;height:44px;border:2px solid #4a6fa5}
</style>
</head>
<body>

<!-- FRONT SIDE -->
<section class="flyer flyer--front">
  <svg class="hero" width="454" height="250" viewBox="0 0 454 250">
    <defs>
      <linearGradient id="frontPhoto" x1="0" y1="0" x2="1" y2="1">
        <stop offset="0" stop-color="#f4f6f8"/>
        <stop offset=".5" stop-color="#c8d0d6"/>
        <stop offset="1" stop-color="#6c757c"/>
      </linearGradient>
    </defs>
    <path role="img" aria-label="Photo of a security camera and an alarm keypad" d="M0 0H454V150Q227 300 0 150Z" fill="url(#frontPhoto)"/>
    <path d="M0 150Q227 300 454 150V166Q227 258 0 166Z" fill="var(--orange)"/>
  </svg>

  <div class="abs brand-block">
    <div class="brand-name"><span class="brand-mark"></span>K P Guard Services</div>
  </div>

  <div class="abs price-label" style="left:37px;top:278px">Intruder Alarms<br>starting from</div>
  <div class="abs price-ring" style="left:35px;top:318px">
    <svg width="100" height="104" viewBox="0 0 100 104">
      <path d="M6 42A46 46 0 0 1 94 42A46 38 0 0 0 6 42Z" fill="var(--orange)"/>
      <path d="M6 62A46 46 0 0 0 94 62A46 38 0 0 1 6 62Z" fill="var(--orange)"/>
    </svg>
    <div class="price">£495 +<br>VAT</div>
  </div>

  <div class="abs price-label" style="left:37px;top:424px">CCTV Systems<br>starting from</div>
  <div class="abs price-ring price-ring--cctv" style="left:28px;top:460px;width:110px;height:110px">
    <svg width="110" height="110" viewBox="0 0 110 110">
      <path d="M6 42A49 46 0 0 1 104 42A49 38 0 0 0 6 42Z" fill="var(--orange)"/>
      <path d="M6 68A49 46 0 0 0 104 68A49 38 0 0 1 6 68Z" fill="var(--orange)"/>
    </svg>
    <div class="price">£595 + VAT<br>(based on 2<br>cameras)</div>
  </div>

  <p class="abs tagline">K P Guard Services are always there, always available, wherever and whenever you need us.</p>

  <p class="abs switch-offer">Not happy with your current provider? Free of charge no obligation take over survey and quotation and up to £100 off</p>

  <div class="abs discount-box">£150 discount on installations<br>*terms and conditions apply</div>

  <footer class="footer">
    <div class="phone">
      <svg width="22" height="24" viewBox="0 0 24 24" fill="none" stroke="var(--white)" stroke-width="1.6"><path d="M6 2l3 5-2 2c1 3 4 6 7 7l2-2 5 3-2 4C11 21 3 13 2 4z"/></svg>
      <b>01632 480913</b>
    </div>
    <div class="contact">
      <div class="contact-row"><svg width="11" height="12" viewBox="0 0 12 14"><path d="M6 0a5 5 0 0 1 5 5c0 4-5 9-5 9S1 9 1 5a5 5 0 0 1 5-5z" fill="var(--ink)"/><circle cx="6" cy="5" r="2" fill="var(--white)"/></svg>14 Hartwell Lane, Brentwood, Essex, CM15-2QX</div>
      <div class="contact-row"><svg width="12" height="10" viewBox="0 0 12 10" fill="none" stroke="var(--ink)" stroke-width="1.4"><rect x="1" y="1" width="10" height="8"/><path d="M1 1l5 4 5-4"/></svg>operations@kpguardservices.co.uk</div>
      <div class="contact-row"><svg width="12" height="12" viewBox="0 0 12 12" fill="none" stroke="var(--ink)" stroke-width="1"><circle cx="6" cy="6" r="5"/><ellipse cx="6" cy="6" rx="2.2" ry="5"/><path d="M1 6h10"/></svg>www.kpguardservices.co.uk</div>
    </div>
  </footer>
</section>

<!-- BACK SIDE -->
<section class="flyer flyer--back">
  <svg class="hero" width="458" height="290" viewBox="0 0 458 290">
    <defs>
      <linearGradient id="backPhoto" x1="0" y1="0" x2="1" y2="1">
        <stop offset="0" stop-color="#dfe6ea"/>
        <stop offset=".6" stop-color="#eef1f3"/>
        <stop offset="1" stop-color="#c9cfd3"/>
      </linearGradient>
      <linearGradient id="devices" x1="0" y1="0" x2="0" y2="1">
        <stop offset="0" stop-color="#4a5560"/>
        <stop offset="1" stop-color="#1f252b"/>
      </linearGradient>
    </defs>
    <path role="img" aria-label="Photo of a wall-mounted alarm touch panel in a bright room" d="M0 0H458V150Q330 280 220 262Q110 248 0 154Z" fill="url(#backPhoto)"/>
    <path d="M0 154Q110 248 220 262Q330 280 458 150V164Q330 258 220 250Q110 240 0 166Z" fill="var(--orange)" transform="translate(0,8)"/>
    <rect role="img" aria-label="Illustration of two smartphones showing the alarm app" x="240" y="130" width="136" height="158" rx="14" fill="url(#devices)"/>
  </svg>

  <h1 class="abs headline">Are you looking to keep you and your premises safe?</h1>

  <div class="abs back-brand"><span class="brand-mark"></span>K P Guard</div>

  <ul class="abs points" style="left:28px;top:303px;width:190px">
    <li style="margin-bottom:14px">K P Guard Services install, maintain and repair all intruder alarms, CCTV, intercom and access control</li>
    <li style="margin-bottom:18px">View, control and manage your security systems anywhere in the world</li>
    <li style="margin-bottom:18px">Feel at ease with monitoring services &amp; police response tailored to suit you and your business</li>
    <li>K P Guard can takeover any existing security system and offer maintenance checks to guarantee the best performance for you and your premises</li>
  </ul>

  <ul class="abs points" style="left:210px;top:303px;width:238px">
    <li style="margin-bottom:23px">K P Guard understand that being security conscious is ever increasing, protecting your property and family is a number one priority</li>
    <li style="margin-bottom:23px">Our fully insured and accredited team offer quality, safety and cost efficiency throughout the whole process</li>
    <li style="margin-bottom:14px">K P Guard Services are using the latest cloud-based technology to stay connected with your home and business 24/7</li>
    <li>If you are looking to improve the security in your home, office or commercial property then call a member of our team today for a free quote.</li>
  </ul>

  <div class="abs badges">
    <div class="badge-lister"><small>Proud members of</small><b>Jobrater</b></div>
    <div class="badge"><i></i>CCTV Systems</div>
    <div class="badge"><i></i>Intruder Alarm Systems</div>
    <div class="badge badge--square"><i></i></div>
  </div>

  <footer class="footer" style="height:76px">
    <div class="phone" style="width:196px">
      <svg width="22" height="24" viewBox="0 0 24 24" fill="none" stroke="var(--white)" stroke-width="1.6"><path d="M6 2l3 5-2 2c1 3 4 6 7 7l2-2 5 3-2 4C11 21 3 13 2 4z"/></svg>
      <b>01632 480913</b>
    </div>
    <div class="contact" style="left:198px">
      <div class="contact-row"><svg width="11" height="12" viewBox="0 0 12 14"><path d="M6 0a5 5 0 0 1 5 5c0 4-5 9-5 9S1 9 1 5a5 5 0 0 1 5-5z" fill="var(--ink)"/><circle cx="6" cy="5" r="2" fill="var(--white)"/></svg>14 Hartwell Lane, Brentwood, Essex, CM15-2QX</div>
      <div class="contact-row"><svg width="12" height="10" viewBox="0 0 12 10" fill="none" stroke="var(--ink)" stroke-width="1.4"><rect x="1" y="1" width="10" height="8"/><path d="M1 1l5 4 5-4"/></svg>operations@kpguardservices.co.uk</div>
      <div class="contact-row"><svg width="12" height="12" viewBox="0 0 12 12" fill="none" stroke="var(--ink)" stroke-width="1"><circle cx="6" cy="6" r="5"/><ellipse cx="6" cy="6" rx="2.2" ry="5"/><path d="M1 6h10"/></svg>www.kpguardservices.co.uk</div>
    </div>
  </footer>
</section>

</body>
</html>
```